Business Card New Design for Veltrix

We would like a new look on our business card, using the same style, the same colors blue, gray and white with similar font that is represented on the new Sell Sheet. We recently re-designed our Sell Sheets - I've attached a sell sheet file for your reference. I've also attached our current business card and our logo. Keep the same information listed on each side of the card.

Contact Information for Business Card

Use details given on example provided

Font styles to use
Other font styles liked:
• Myriad Regular and Bold

Colors

Designer to choose colors to be used in the design.

Requirements
Must have
• Current Information that was provided on the current business card. Colors Must use Blue, Gray and White, the same colors as the sell sheet example.

```html
<!DOCTYPE html>
<html lang="en">
<head>
<meta charset="utf-8">
<title>Veltrix Business Card</title>
<link href="https://fonts.googleapis.com/css2?family=Source+Sans+3:wght@400;600;700&family=Michroma&display=swap" rel="stylesheet">
<style>
  :root {
    --backdrop: #3a3634;
    --card-white: #f6f7f8;
    --brand-blue: #1f5fb0;
    --brand-blue-deep: #0f4a9a;
    --brand-blue-light: #2f7ad0;
    --ink-gray: #3c3c3e;
    --logo-gray: #5a5c60;
    --rule-gray: #d4d6d9;
    --back-text: #e8eef8;
  }
  * { margin: 0; padding: 0; box-sizing: border-box; }
  html, body { width: 1200px; height: 844px; overflow: hidden; }
  body {
    background: var(--backdrop);
    font-family: "Source Sans 3", "Myriad Pro", sans-serif;
    position: relative;
  }
  .card {
    position: absolute;
    top: 268px;
    width: 540px;
    height: 308px;
    border-radius: 3px;
    box-shadow: 0 10px 30px rgba(0,0,0,.45);
    overflow: hidden;
  }
  .card-front { left: 40px; background: var(--card-white); }
  .card-back {
    left: 620px;
    background: linear-gradient(160deg, var(--brand-blue-light) 0%, var(--brand-blue) 50%, var(--brand-blue-deep) 100%);
  }

  /* front */
  .brand-name {
    position: absolute;
    top: 58px;
    right: 44px;
    font-weight: 700;
    font-size: 50px;
    letter-spacing: 6px;
    color: var(--logo-gray);
    line-height: 1;
  }
  .brand-rule {
    position: absolute;
    top: 134px;
    left: 40px;
    right: 40px;
    height: 1px;
    background: var(--rule-gray);
  }
  .person {
    position: absolute;
    left: 40px;
    top: 156px;
    color: var(--ink-gray);
    font-size: 15px;
    line-height: 19px;
  }
  .person-name {
    font-family: "Michroma", sans-serif;
    color: var(--brand-blue);
    font-size: 17px;
    letter-spacing: 2px;
    line-height: 22px;
  }
  .person-title { font-size: 13px; margin-bottom: 2px; }
  .company { color: var(--brand-blue); }
  .accent { color: var(--brand-blue); }
  .contacts {
    position: absolute;
    right: 40px;
    top: 160px;
    text-align: right;
    font-size: 14.5px;
    line-height: 20px;
    color: var(--ink-gray);
  }
  .contact-label { color: var(--brand-blue); font-weight: 700; }

  /* back */
  .product-list {
    list-style: none;
    position: absolute;
    inset: 0;
    display: flex;
    flex-direction: column;
    justify-content: center;
    align-items: center;
    font-family: "Michroma", sans-serif;
    font-size: 11.5px;
    letter-spacing: 2px;
    line-height: 21px;
    color: var(--back-text);
    text-transform: uppercase;
  }
</style>
</head>
<body>
  <section class="card card-front" aria-label="Business card front">
    <div class="brand-name">VELTRIX</div>
    <div class="brand-rule"></div>
    <div class="person">
      <div class="person-name">DANIEL MARSH</div>
      <div class="person-title">CEO</div>
      <div class="company">Veltrix Technical Services, Inc</div>
      <div>4170 Harbor Mill Road</div>
      <div>Lakeview, IL 60199</div>
      <div>www.<span class="accent">vtx-ts</span>.com</div>
      <div>dmarsh@<span class="accent">vtx-ts</span>.com</div>
    </div>
    <div class="contacts">
      <div><span class="contact-label">Toll Free</span> (888) 555-0172 x214</div>
      <div><span class="contact-label">Phone</span> (815) 555-0172</div>
      <div><span class="contact-label">Direct</span> (815) 555-0139</div>
      <div><span class="contact-label">Cell</span> (815) 555-0186</div>
    </div>
  </section>

  <section class="card card-back" aria-label="Business card back">
    <ul class="product-list">
      <li>Conveyors</li>
      <li>Target Sauce Applicators</li>
      <li>Target Topping Applicators</li>
      <li>Waterfall Topping Applicators</li>
      <li>Pepperoni / Meat Slicer / Applicators</li>
      <li>Portion Controlled Filler Pumps</li>
      <li>Dry Ingredient Applicators</li>
      <li>Check Weigh Conveyors</li>
      <li>Portion Compensators</li>
    </ul>
  </section>
</body>
</html>
```